Packaging design for a modern organic cosmetic product

We are an organic cosmetic brand using Aloe Vera. We are looking for new packaging design for cardboard tubes similar to the following:
https://img7.pelmorastatic.net/kf/Q4ba183c72d904617ae2093541cf62b08K.jpg
This package will be used to insert 2 or 3 products as a combo.
The printing will be done in two colors. We just need a base design for the tube and the cap. Later a sticker may be stick on the tube to specify the content of the combo. So the design should be workable with or without an additional sticker. At this time we are only looking for the base tube design with some artwork without the sticker design. The artwork can be based on our logo, color and theme. Our logo is attached herewith. Our company is located in the Algarve, South Portugal. Our products are regional and related to Sea, Sunshine, Sand and Aloe Vera. The products are based on natural ingredients, vegan and organic.
Please let me know if you have any questions. I am also attaching the vector file of the logo.

```html
<!DOCTYPE html>
<html lang="en">
<head>
<meta charset="utf-8">
<title>Solmara – Tube Label and Cap</title>
<link rel="stylesheet" href="https://fonts.googleapis.com/css2?family=Josefin+Sans:wght@400&family=Archivo:ital,wght@1,800&display=swap">
<style>
  :root {
    --olive-deep: #3d4422;
    --olive-mid: #5a6434;
    --aloe-light: #c2cb84;
    --aloe-pale: #d3da9e;
    --backdrop: #e6e7e3;
    --sticker-ink: #aab26f;
    --sticker-line: #7f8752;
  }
  * { margin: 0; padding: 0; box-sizing: border-box; }
  html, body {
    width: 704px; height: 1200px; overflow: hidden;
    background: var(--backdrop);
  }
  .artboard {
    position: relative; width: 704px; height: 1200px;
  }
  .cap-top {
    position: absolute; left: 36px; top: 470px;
    width: 264px; height: 264px; border-radius: 50%;
    background: var(--olive-deep);
    box-shadow: 4px 6px 10px rgba(0,0,0,.18);
    display: flex; align-items: center; justify-content: center;
  }
  .tube-wrap {
    position: absolute; left: 330px; top: 360px;
    width: 340px; height: 486px;
    box-shadow: 6px 8px 12px rgba(0,0,0,.28);
    overflow: hidden;
  }
  .tube-wrap svg.artwork { position: absolute; inset: 0; }
  .brand-name {
    font-family: "Josefin Sans", sans-serif;
    font-weight: 400; font-size: 26px;
    letter-spacing: 0.28em; text-indent: 0.28em;
    text-transform: uppercase;
  }
  .cap-top .brand-name { color: var(--aloe-light); }
  .tube-brand {
    position: absolute; left: 0; right: 0; top: 190px;
    text-align: center; color: var(--olive-deep);
  }
  .sticker-zone {
    position: absolute; left: 62px; top: 302px;
    width: 168px; height: 86px;
    border: 1px solid var(--sticker-line);
    display: flex; align-items: center; justify-content: center;
  }
  .sticker-zone span {
    font-family: "Archivo", sans-serif; font-style: italic; font-weight: 800;
    font-size: 28px; color: var(--sticker-ink);
  }
</style>
</head>
<body>
<main class="artboard">
  <section class="cap-top" aria-label="Cap top design">
    <span class="brand-name">Solmara</span>
  </section>

  <section class="tube-wrap" aria-label="Tube wrap design">
    <svg class="artwork" width="340" height="486" viewBox="0 0 340 486" aria-hidden="true">
      <rect width="340" height="486" fill="var(--olive-deep)"/>
      <path d="M0 250 C 40 110, 170 20, 340 0 L340 486 L0 486 Z" fill="var(--olive-mid)" opacity=".6"/>
      <path d="M0 290 C 30 120, 190 10, 340 20 L340 486 L0 486 Z" fill="var(--aloe-pale)" opacity=".55"/>
      <ellipse cx="260" cy="240" rx="250" ry="300" transform="rotate(-18 260 240)" fill="var(--aloe-light)"/>
      <path d="M340 330 C 300 420, 230 470, 150 486 L340 486 Z" fill="var(--olive-deep)"/>
      <path d="M340 350 C 310 420, 250 465, 180 486" stroke="var(--aloe-pale)" stroke-width="6" fill="none" opacity=".6"/>
    </svg>
    <div class="brand-name tube-brand">Solmara</div>
    <div class="sticker-zone"><span>STICKER</span></div>
  </section>
</main>
</body>
</html>
```